Chauffeur Car Driver Needing a design with/without logo for business cards

I'm a chauffeur car driver in Melbourne Australia. I have an extensive list of personal customers and need to provide a professional business card to new customers.
My business name is 'RivaPlus'.
I offer a personalised service to customer who need a transport alternative to taxis. I don't want it to look too 'upmarket' as i don't want it to seem too expensive or only for special occasions. The majority of my clients are business professionals who use me for airport transfers.
I definitely don't want the card/logo to have an image of a car/road etc. I prefer something abstract. A 'pencil-line'-type font will grab my attention but not absolutely necessary. Not too 'digital' or 'ultra - modern' looking.
I need the card to display the following information
Riva Plus - main logo/text
Chauffeur Cars - sub text
Marco Devilles
0452 918 306
bookings@RivaPlus.example.au
I would like the focus to be on 'RivaPlus' with everything else smaller.
Look forward to seeing ideas!!!!
Target Market(s)
Business Corporate Professionals
Industry/Entity Type
Airport
Requirements
Nice to have
- Pencil line type font
Should not have
- Images of cars, road, tyres, steering wheel etc.

```html
<!DOCTYPE html>
<html lang="en">
<head>
<meta charset="utf-8">
<title>RivaPlus Chauffeur Cars – Business Cards</title>
<link rel="stylesheet" href="https://fonts.googleapis.com/css2?family=Source+Serif+4:wght@400;600&display=swap">
<style>
  :root {
    --page-bg: #2a2a2c;
    --card-dark: #050505;
    --card-light: #ffffff;
    --silver: #d9d9d9;
    --ink: #111111;
    --ink-soft: #333333;
    --ghost: #e6e6e6;
  }
  * { margin: 0; padding: 0; box-sizing: border-box; }
  html, body {
    width: 977px;
    height: 1200px;
    overflow: hidden;
    background: var(--page-bg);
    font-family: "Source Serif 4", Georgia, serif;
  }
  .canvas {
    position: relative;
    width: 977px;
    height: 1200px;
  }
  .card {
    position: absolute;
    overflow: hidden;
  }
  .card--front {
    left: 200px;
    top: 90px;
    width: 650px;
    height: 400px;
    background: var(--card-dark);
  }
  .card--back {
    left: 125px;
    top: 600px;
    width: 700px;
    height: 425px;
    background: var(--card-light);
  }
  .brand-name {
    position: absolute;
    font-weight: 400;
    white-space: nowrap;
    line-height: 1;
  }
  .front-mark {
    left: 0;
    right: 0;
    top: 130px;
    text-align: center;
    font-size: 112px;
    color: var(--silver);
  }
  .tagline {
    position: absolute;
    left: 0;
    right: 0;
    bottom: 52px;
    text-align: center;
    font-size: 19px;
    letter-spacing: 0.55em;
    padding-left: 0.55em;
    color: var(--card-light);
  }
  .back-mark {
    left: 70px;
    top: 105px;
    font-size: 112px;
    color: var(--ink);
    z-index: 1;
  }
  .ghost-mark {
    right: -8px;
    top: 14px;
    writing-mode: vertical-rl;
    font-size: 104px;
    color: var(--ghost);
    z-index: 0;
  }
  .contact {
    position: absolute;
    left: 72px;
    top: 290px;
    color: var(--ink);
    z-index: 1;
  }
  .contact__name {
    font-size: 21px;
    font-weight: 600;
    margin-bottom: 6px;
  }
  .contact__details {
    font-size: 20px;
    color: var(--ink-soft);
  }
  .contact__divider {
    margin: 0 6px;
  }
</style>
</head>
<body>
  <main class="canvas">
    <section class="card card--front" aria-label="Business card front">
      <p class="brand-name front-mark">RivaPlus</p>
      <p class="tagline">CHAUFFEUR CARS</p>
    </section>

    <section class="card card--back" aria-label="Business card back">
      <p class="brand-name ghost-mark" aria-hidden="true">RivaPlus</p>
      <p class="brand-name back-mark">RivaPlus</p>
      <div class="contact">
        <p class="contact__name">Marco Devilles</p>
        <p class="contact__details">0452 918 306<span class="contact__divider">|</span>bookings@RivaPlus.example.au</p>
      </div>
    </section>
  </main>
</body>
</html>
```